we are an outdoor outlet in a country club that has a variety of outlets. The Club is called Brookhaven and is located in Cairo, Egypt. This garden menu will include cuisines from the Mediterranean, Asia and Texmex. we need a menu that is colorful and would fit an A3 size, back and front are to be used. Attached is the old menu currently in use (Garden Menu 2012.pdf is just for reference) and the new menu text for you to use is under the name Garden Menu Fall 2013
thank you.

```html
<!DOCTYPE html>
<html lang="en">
<head>
<meta charset="utf-8">
<title>Garden Menu Fall 2013 – Brookhaven</title>
<link rel="stylesheet" href="https://fonts.googleapis.com/css2?family=Kaushan+Script&family=Open+Sans:wght@400;700&family=Lora:ital,wght@1,700&display=swap">
<style>
:root{
  --cream:#fdf8ec;
  --orange:#ec7a1c;
  --orange-deep:#d35f12;
  --green:#6a9a2a;
  --brown:#4a2a12;
  --ink:#2e2418;
}
html,body{margin:0;padding:0;overflow:hidden;}
body{width:849px;height:1200px;background:#fff;}
.menu{position:relative;width:849px;height:1200px;background:var(--cream);
  border-left:8px solid var(--orange);box-sizing:border-box;overflow:hidden;
  font-family:"Open Sans",Arial,sans-serif;color:var(--ink);}
.menu-title{position:absolute;left:28px;top:14px;margin:0;font-family:"Kaushan Script",cursive;
  font-size:46px;font-weight:400;color:var(--orange);}
.brand{position:absolute;right:36px;top:26px;display:flex;align-items:center;gap:10px;}
.brand-dot{width:34px;height:34px;border-radius:50%;background:var(--orange);}
.brand-name{font-family:"Open Sans",Arial,sans-serif;font-weight:700;font-size:34px;color:var(--green);}
.corner-title{position:absolute;left:24px;top:118px;margin:0;font-family:"Lora",serif;font-style:italic;
  font-weight:700;font-size:25px;color:var(--brown);border-bottom:3px solid var(--green);padding-bottom:2px;}
.column{position:absolute;display:flex;flex-direction:column;justify-content:space-between;}
.col-left{left:24px;top:160px;width:396px;height:1028px;}
.col-right{left:436px;top:116px;width:395px;height:1072px;}
.section{display:flow-root;}
.section h3{margin:0 0 3px;font-weight:700;font-size:23px;line-height:30px;color:var(--orange-deep);}
.section ul{list-style:none;margin:0;padding:0;}
.section li{font-size:11.4px;line-height:15px;margin-bottom:3px;}
.price{white-space:nowrap;}
.photo{float:right;border-radius:4px;margin:4px 0 6px 14px;}
.photo-soup{width:135px;height:120px;background:linear-gradient(135deg,#c6a05a,#7e6a2e 60%,#4f5a26);}
.photo-starter{width:140px;height:120px;margin-top:10px;background:linear-gradient(135deg,#a9c36a,#d45a2a 55%,#e6d6b4);}
.photo-salad{width:140px;height:115px;background:linear-gradient(135deg,#6f9a34,#c9402a 50%,#eee6cf);}
.photo-pizza{width:175px;height:130px;margin-top:0;background:linear-gradient(135deg,#e0a64a,#b83a1e 55%,#6a4a22);}
.main-courses ul{width:200px;}
.art-umbrella{position:absolute;left:652px;top:930px;width:189px;height:270px;
  background:linear-gradient(180deg,#e86a2a 0%,#f0a23c 35%,#f4e6c6 70%,#c9a56a 100%);}
</style>
</head>
<body>
<main class="menu">
  <h1 class="menu-title">Garden Menu Fall 2013</h1>
  <div class="brand"><span class="brand-dot"></span><span class="brand-name">Brookhaven</span></div>
  <h2 class="corner-title">Mediterranean Corner</h2>

  <div class="column col-left">
    <section class="section soups">
      <h3>Soups</h3>
      <div class="photo photo-soup" role="img" aria-label="Bowl of soup"></div>
      <ul>
        <li>Tomato Basil.........<span class="price">00.00 L.E.</span></li>
        <li>Simmered tomato soup finished with fresh basil and cream......<span class="price">00.00 L.E.</span></li>
        <li>Chicken Cream......<span class="price">00.00 L.E.</span></li>
        <li>Chicken broth with roasted chicken cubes, pine nuts, and cream......<span class="price">00.00 L.E.</span></li>
        <li>Moroccan Harira......<span class="price">00.00 L.E.</span></li>
        <li>Vegetable broth with fresh tomato, chickpeas, lentil, cilantro, and diced lamb......<span class="price">00.00 L.E.</span></li>
      </ul>
    </section>

    <section class="section appetizers">
      <h3>Appetizers</h3>
      <div class="photo photo-starter" role="img" aria-label="Plated appetizer"></div>
      <ul>
        <li>Salmontartare seasoned with lemon juice, garlic, and crushed black pepper......<span class="price">00.00 L.E.</span></li>
        <li>Roasted eggplant rolls with herbed ricotta cheese and pine nuts......<span class="price">00.00 L.E.</span></li>
        <li>Falafel in mini pita served with tahina and oriental salsa......<span class="price">00.00 L.E.</span></li>
        <li>Mankousha with thyme and olive oil......<span class="price">00.00 L.E.</span></li>
        <li>Fried kobeba with minced meat, spices, and pine nuts......<span class="price">00.00 L.E.</span></li>
        <li>Fried calamari a la Romana served with aioli......<span class="price">00.00 L.E.</span></li>
        <li>Sambousek with herbed white cheese and mint......<span class="price">00.00 L.E.</span></li>
        <li>Oriental sausage sautéed with garlic and onion......<span class="price">00.00 L.E.</span></li>
        <li>Mini vine leaves with a yoghurt dip......<span class="price">00.00 L.E.</span></li>
        <li>Fatouch with a pomegranate syrup dressing......<span class="price">00.00 L.E.</span></li>
        <li>Hummus seasoned with lemon juice, garlic, and olive oil......<span class="price">00.00 L.E.</span></li>
        <li>White cheese with diced tomato, thyme, and olive oil......<span class="price">00.00 L.E.</span></li>
        <li><div class="photo photo-salad" role="img" aria-label="Fresh salad"></div>Tehina seasoned with cumin, lemon juice, and garlic......<span class="price">00.00 L.E.</span></li>
      </ul>
    </section>

    <section class="section salads">
      <h3>Salads</h3>
      <ul>
        <li>Caprese......<span class="price">00.00 L.E.</span></li>
        <li>Buffalo mozzarella and sliced tomato with a balsamic vinaigrette......<span class="price">00.00 L.E.</span></li>
      </ul>
    </section>
  </div>

  <div class="column col-right">
    <section class="section salads-more">
      <ul>
        <li>Rocket Apple......<span class="price">00.00 L.E.</span></li>
        <li>Rocket leaves with gorgonzola, croutons, and strawberry vinaigrette......<span class="price">00.00 L.E.</span></li>
        <li>French Riviera Niçoise......<span class="price">00.00 L.E.</span></li>
        <li>Lettuce, egg, tomato, tuna, olives, onion, celery, radish, bell pepper in a French vinaigrette......<span class="price">00.00 L.E.</span></li>
        <li>Folie......<span class="price">00.00 L.E.</span></li>
        <li>Mixed greens with crab sticks, mushroom, corn, cherry tomato in a mango vinaigrette......<span class="price">00.00 L.E.</span></li>
      </ul>
    </section>

    <section class="section pizza-pasta">
      <div class="photo photo-pizza" role="img" aria-label="Pizza"></div>
      <h3>Pizza &amp; Pasta</h3>
      <ul>
        <li>Pizza Margarita (Choose your toppings)......<span class="price">00.00 L.E.</span></li>
        <li>Create your own pasta</li>
        <li>Type: Spaghetti, Tagliatelle, Penne......<span class="price">00.00 L.E.</span></li>
        <li>Sauces: Napolitana, Bolognese, Alfredo......<span class="price">00.00 L.E.</span></li>
      </ul>
    </section>

    <section class="section toppings">
      <h3>Toppings</h3>
      <ul>
        <li>Bell peppers, olives, tomato, onion......<span class="price">00.00 L.E.</span></li>
        <li>Mushroom, chicken, tuna, pepperoni......<span class="price">00.00 L.E.</span></li>
        <li>Smoked salmon, shrimps......<span class="price">00.00 L.E.</span></li>
        <li>Lasagna......<span class="price">00.00 L.E.</span></li>
      </ul>
    </section>

    <section class="section sandwiches">
      <h3>Sandwiches</h3>
      <ul>
        <li>(Served with French fries or a garden salad)</li>
        <li>Beef or chicken Shawerma......<span class="price">00.00 L.E.</span></li>
        <li>Grilled kofta......<span class="price">00.00 L.E.</span></li>
        <li>Greek lamb gyro in pita bread with Tzatziki......<span class="price">00.00 L.E.</span></li>
        <li>Club sandwich with smoked beef, turkey, egg......<span class="price">00.00 L.E.</span></li>
      </ul>
    </section>

    <section class="section main-courses">
      <h3>Main Courses</h3>
      <ul>
        <li>Veal Parmegiana......<span class="price">00.00 L.E.</span></li>
        <li>Breaded veal escalope topped with melted cheese and tomato sauce served with Spaghetti......<span class="price">00.00 L.E.</span></li>
        <li>Chicken a la Francaise......<span class="price">00.00 L.E.</span></li>
        <li>Pan fried chicken breast in a mushroom cream sauce with vegetables white rice......<span class="price">00.00 L.E.</span></li>
        <li>Grilled Salmon......<span class="price">00.00 L.E.</span></li>
        <li>Salmon steak charcoal grilled with avocado tomato relish and creamy mushroom risotto......<span class="price">00.00 L.E.</span></li>
        <li>Moroccan Chicken......<span class="price">00.00 L.E.</span></li>
        <li>Chicken cubes simmered with spices and olives served with tomato rice......<span class="price">00.00 L.E.</span></li>
        <li>Filet......<span class="price">00.00 L.E.</span></li>
        <li>Tender filet grilled to your liking served with mashed potato and creamed spinach......<span class="price">00.00 L.E.</span></li>
        <li>Choice of sauces: Brown mushroom, Green Peppercorn, Gorgonzola......<span class="price">00.00 L.E.</span></li>
      </ul>
    </section>
  </div>

  <div class="art-umbrella" role="img" aria-label="Illustration of a garden umbrella over a table"></div>
</main>
</body>
</html>
```